Structural Engineering Company needs ad for magazine

We are an engineering office for structural engineering in the entertainment industry. Our focus are concert stages, festival structures, grand stands and exhibition booths. Our customers are mainly from Europe, we realize the projects worldwide. Typical customers are designer, architects, stage builders, exhibition builder and technical service provider. We are creating structural analyses, technical consulting, technical drawings and risk assessment. We are working on mid size and major events.
Some technical notes:
- CMYK profile needed, minimum 300 dpi for raster graphic
- Our primary color is Petrol. Favourite is petrol, coral and grey (black). Please use palette shown below.
- Our font in documents is Myriad. Regular at 10 pt for text and Light at 16-24pt for titles.
- The format for the ad is 61 x 127 mm (portrait) or 185 x 46 mm (landscape). Which one is up to you.
To the content:
- For contact details we just want to provide our web address "belsokar.de" and/or our e-mail "info@belsokar.de"
- Attached are some Logo files and photos.
- The ad do not advertise a specific product. It is more a general advertisement for the company.
- The language for the ad should be German. Below are keywords in English and corresponding German translation. You do not need to place all Keywords, it is just a brainstorming list to help you. You are also welcome to use other text. We will help with translation, if necessary.
- we like discussing ideas to get better results, so also if you have questions, please ask.
- If you need information that we haven't thought of yet, please ask.
Our slogan (also in Germany): event meets engineering
Service Keywords EN / DE
- Structural Analysis / Statische Berechnungen
- Risk Assessment / Risikobewertungen
- Consulting & Design / Beratung & Konstruktion
Technical Keywords EN / DE
- Stage machinery / Bühnentechnik
- Scaffolding / Gerüstbau
- Exhibition Booths / Messebauten
- Tents / Zelte
- Temporary Structures / Fliegende Bauten
- Truss / Traversen
- Stages / Bühnen
- Grand Stands / Tribünen
- Leightweight Construction / Leichtbau
- Steel Construction / Stahlbau
- Amusement Rides / Fahrgeschäfte
Look and feel
Each slider illustrates characteristics of the customer's brand and the style your logo design should communicate.

```html
<!DOCTYPE html>
<html lang="de">
<head>
<meta charset="utf-8">
<title>Belsokar – Strukturanalysen für die Unterhaltungstechnik</title>
<link rel="stylesheet" href="https://fonts.googleapis.com/css2?family=Roboto:wght@300;400;700&display=swap">
<style>
  :root {
    --petrol-dark: #0f4a56;
    --petrol: #16697a;
    --petrol-light: #2b8798;
    --coral: #ee6c5b;
    --coral-soft: rgba(238, 108, 91, 0.5);
    --grey-light: #c7cdd0;
    --grey-mid: #8e979b;
    --grey-dark: #3d4447;
    --ink: #1d2224;
    --band: rgba(20, 38, 44, 0.86);
    --white: #ffffff;
  }
  * { margin: 0; padding: 0; box-sizing: border-box; }
  html, body {
    width: 1200px;
    height: 2500px;
    overflow: hidden;
  }
  body {
    position: relative;
    font-family: "Roboto", Arial, sans-serif;
    color: var(--white);
    background: linear-gradient(180deg, var(--petrol) 0%, var(--petrol-light) 700px, var(--petrol-light) 100%);
  }

  .brand {
    position: absolute;
    top: 150px;
    left: 0;
    width: 1200px;
    display: flex;
    justify-content: center;
    align-items: center;
    gap: 28px;
  }
  .brand-mark {
    width: 40px;
    height: 40px;
    border-radius: 50%;
    background: var(--coral);
  }
  .brand-name {
    font-weight: 400;
    font-size: 78px;
    letter-spacing: 14px;
    line-height: 1;
  }

  .headline {
    position: absolute;
    top: 392px;
    left: 0;
    width: 1200px;
    text-align: center;
    font-size: 76px;
    font-weight: 300;
    line-height: 100px;
  }
  .headline strong { font-weight: 700; }

  .stage-photo {
    position: absolute;
    top: 640px;
    left: 0;
    width: 1200px;
    height: 810px;
    background:
      linear-gradient(180deg, rgba(43,135,152,0) 0%, rgba(43,135,152,0.6) 10%, rgba(199,205,208,0.0) 30%),
      radial-gradient(ellipse 300px 200px at 50% 72%, rgba(238,108,91,0.28), transparent 70%),
      linear-gradient(180deg, var(--petrol-light) 0%, var(--grey-light) 18%, var(--grey-mid) 55%, var(--grey-dark) 88%, var(--ink) 100%);
  }

  .night-photo {
    position: absolute;
    top: 1450px;
    left: 0;
    width: 1200px;
    height: 1050px;
    background:
      radial-gradient(ellipse 520px 320px at 18% 92%, var(--coral-soft), transparent 70%),
      radial-gradient(ellipse 560px 420px at 82% 38%, rgba(199,205,208,0.28), transparent 70%),
      linear-gradient(180deg, var(--petrol-dark) 0%, #173e46 55%, var(--ink) 100%);
  }

  .keywords {
    position: absolute;
    top: 1450px;
    left: 0;
    width: 1200px;
    height: 233px;
    background: var(--band);
    display: flex;
    flex-direction: column;
    justify-content: center;
    text-align: center;
    font-size: 39px;
    font-weight: 300;
    line-height: 50px;
  }

  .services {
    position: absolute;
    top: 1750px;
    left: 110px;
    list-style: none;
    font-size: 80px;
    font-weight: 300;
    line-height: 125px;
  }
  .services strong { font-weight: 700; }

  .contact {
    position: absolute;
    top: 2240px;
    left: 355px;
    padding-left: 30px;
    border-left: 4px solid var(--coral);
    font-size: 39px;
    line-height: 58px;
  }
  .contact-title { font-weight: 700; font-size: 40px; }
  .contact-line { display: flex; align-items: center; gap: 16px; }
  .contact-web { font-weight: 700; }
  .contact-mail { font-weight: 300; }
  .contact-line svg { width: 36px; height: 36px; flex: none; }
</style>
</head>
<body>
  <div class="brand">
    <span class="brand-mark"></span>
    <span class="brand-name">BELSOKAR</span>
  </div>

  <h1 class="headline"><strong>Strukturanalysen</strong> für<br>die Unterhaltungstechnik</h1>

  <div class="stage-photo" role="img" aria-label="Foto: Festivalbühne mit Bildschirmen, Traversen und jubelndem Publikum unter blauem Himmel"></div>
  <div class="night-photo" role="img" aria-label="Foto: unscharfe Nahaufnahme einer Aluminiumtraverse mit Scheinwerfer im Bühnenlicht"></div>

  <div class="keywords">
    <p>Bühnentechnik · Gerüstbau · Messebauten</p>
    <p>Zelte · Fliegende Bauten · Traversen · Bühnen</p>
    <p>Tribünen · Leichtbau · Stahlbau · Fahrgeschäfte</p>
  </div>

  <ul class="services">
    <li><strong>Statische</strong> Berechnungen</li>
    <li><strong>Risikobewertungen</strong></li>
    <li><strong>Beratung</strong> &amp; Konstruktion</li>
  </ul>

  <div class="contact">
    <p class="contact-title">KONTAKTIERE UNS</p>
    <p class="contact-line contact-web">
      <svg viewBox="0 0 24 24" fill="none" stroke="#ffffff" stroke-width="2" aria-hidden="true">
        <circle cx="12" cy="12" r="10"/>
        <ellipse cx="12" cy="12" rx="4.5" ry="10"/>
        <line x1="2" y1="12" x2="22" y2="12"/>
        <path d="M4 6.5h16M4 17.5h16"/>
      </svg>
      belsokar.de
    </p>
    <p class="contact-line contact-mail">
      <svg viewBox="0 0 24 24" fill="none" stroke="#ffffff" stroke-width="1.8" aria-hidden="true">
        <rect x="2" y="5" width="20" height="14"/>
        <path d="M2 5l10 8 10-8M2 19l7.5-7M22 19l-7.5-7"/>
      </svg>
      info@belsokar.de
    </p>
  </div>
</body>
</html>
```